VORIK FLYER 2019

Hi, We need an A4 flyer design for our cleaning company, focusing on dry carpet cleaning I attached our catalogue to give some idea. In addition, our websites can provide more information. Our Services:-General Cleaning Carry out heavy cleansing tasks and special projects. Clean, stock and supply designated facility areas (dusting, sweeping, vacuuming, mopping, cleaning ceiling vents, restroom cleaning etc).Using electrically powered scrubbing and polishing machines to burnish, scrub, polish and spray clean floors. Window Cleaning Regular, Reliable Window Cleaning. Hard To Reach Windows. Single 7 Multi-Storey. Frames and Glass Cleaned. Floor Cleaning Marble Cleaning & Polishing. Tile & Grout Cleaning. Hardwood Floors Services. Vinyl Floors. The BRAM Dry Extraction Carpet Cleaning System uses environmentally preferred, Blue Crest Certified cleaning products that deep cleans your carpets and textured hard floors quickly and easily.

Target Market(s)

Residential and Commercial.
Offices, Hospitals, Restaurants, Etc.

Industry/Entity Type

Cleaning Service

Font styles to use
Serif
Sans Serif

Colors
33a6d7
0592cd
85cae6
85acd3
3277b5
296eb1

Requirements
Must have
• CREATIVE AND MINIMAL
Nice to have
• Engaging Pics and Texts

```html
<!DOCTYPE html>
<html lang="en">
<head>
<meta charset="utf-8">
<title>Vorik Cleaning &amp; Maintenance – Flyer</title>
<link href="https://fonts.googleapis.com/css2?family=Oswald:wght@400;500&family=Open+Sans:wght@400;700&display=swap" rel="stylesheet">
<style>
  :root{
    --navy:#1c2a66;
    --navy-light:#2b4796;
    --ink:#23235c;
    --text:#3a3a3a;
    --grey-band:#c9ccd2;
    --grey-frame:#c4c4c4;
    --page:#ececec;
    --white:#ffffff;
    --accent:#3277b5;
  }
  *{box-sizing:border-box;margin:0;padding:0}
  html,body{width:904px;height:1200px;overflow:hidden;background:var(--page)}
  .flyer{position:absolute;left:28px;top:0;width:848px;height:1200px;background:var(--white);overflow:hidden;font-family:"Open Sans",Arial,sans-serif;color:var(--text)}

  .header-band{position:absolute;left:0;top:0;width:100%;height:131px;background:linear-gradient(90deg,var(--navy) 40%,var(--navy-light) 100%)}
  .tagline{position:absolute;right:18px;top:68px;font-family:"Oswald",Arial,sans-serif;font-weight:400;font-size:26px;color:var(--white);letter-spacing:.2px}

  .hero-rim{position:absolute;left:0;top:131px;width:100%;height:425px;background:var(--grey-band);
    clip-path:polygon(0 0,100% 0,100% 398px,50% 425px,0 398px)}
  .hero-photo{position:absolute;left:0;top:131px;width:100%;height:413px;
    background:linear-gradient(180deg,#e4e1da 0%,#cfcac1 45%,#8f8a84 80%,#a39a8e 100%);
    clip-path:polygon(0 0,100% 0,100% 386px,50% 413px,0 386px)}

  .brand-panel{position:absolute;left:0;top:0;width:495px;height:162px;background:var(--white);
    clip-path:polygon(0 0,495px 0,395px 162px,0 162px);filter:drop-shadow(0 2px 3px rgba(0,0,0,.25))}
  .brand-name{position:absolute;left:26px;top:30px;width:340px;font-family:"Oswald",Arial,sans-serif;font-weight:400;font-size:36px;line-height:46px;color:var(--ink);letter-spacing:.5px}

  .services-title{position:absolute;left:26px;top:565px;font-family:"Oswald",Arial,sans-serif;font-weight:400;font-size:28px;color:var(--ink)}
  .service{position:absolute;left:26px;width:509px}
  .service-head{display:flex;align-items:center;gap:14px;height:34px}
  .service-icon{width:34px;height:34px;border:1px solid #bbb;display:flex;align-items:center;justify-content:center}
  .service-name{font-family:"Open Sans",Arial,sans-serif;font-weight:700;font-size:16px;color:var(--ink);text-transform:uppercase}
  .service-text{margin-top:8px;font-size:15.2px;line-height:20.5px;text-align:justify}

  .side-photo{position:absolute;left:579px;width:243px;border:2px solid var(--grey-frame)}
  .side-photo.dusting{top:572px;height:170px;background:linear-gradient(135deg,#f1efe9,#cfc9bd 50%,#d9b84a 75%,#efe9dc)}
  .side-photo.window{top:752px;height:170px;background:linear-gradient(160deg,#dfe7e2,#8fa890 45%,#c9d4cf 75%,#e8ece9)}
  .side-photo.carpet{top:932px;height:172px;background:linear-gradient(150deg,#6f655a,#3b3a3e 45%,#233a6a 65%,#8c7e6a)}

  .footer{position:absolute;left:0;top:1122px;width:100%;height:78px;border-top:3px solid var(--accent);background:var(--grey-band)}
  .footer-phone-band{position:absolute;right:0;top:0;width:303px;height:75px;background:linear-gradient(90deg,var(--navy),var(--navy-light));clip-path:polygon(0 0,100% 0,100% 100%,50px 100%)}
  .cta{position:absolute;left:32px;top:13px;font-family:"Oswald",Arial,sans-serif;font-weight:500;font-size:34px;line-height:46px;color:var(--ink)}
  .phone{position:absolute;right:24px;top:13px;display:flex;align-items:center;gap:12px;font-family:"Oswald",Arial,sans-serif;font-weight:400;font-size:36px;line-height:46px;color:var(--white)}
</style>
</head>
<body>
<div class="flyer">
  <div class="header-band"></div>
  <div class="tagline">RESIDENTIAL AND COMMERCIAL</div>

  <div class="hero-rim"></div>
  <div class="hero-photo" role="img" aria-label="Bright, clean living room with grey sofas, orange cushions, a wooden coffee table and a white lounge chair on a rug"></div>

  <div class="brand-panel">
    <div class="brand-name">VORIK CLEANING<br>&amp; MAINTENANCE</div>
  </div>

  <h2 class="services-title">OUR SERVICES:</h2>

  <section class="service" style="top:622px">
    <div class="service-head">
      <span class="service-icon"><svg width="20" height="24" viewBox="0 0 20 24"><rect x="5" y="9" width="10" height="14" rx="2" fill="var(--ink)"/><rect x="7" y="4" width="6" height="5" fill="var(--ink)"/><path d="M13 5h5" stroke="var(--ink)" stroke-width="2"/></svg></span>
      <h3 class="service-name">General Cleaning</h3>
    </div>
    <p class="service-text">Carry out heavy cleansing tasks and special projects. Clean, stock and supply designated facility areas (dusting, sweeping, vacuuming, mopping, cleaning ceiling vents, restroom cleaning etc). Using electrically powered scrubbing and polishing machines to burnish, scrub, polish and spray clean floors.</p>
  </section>

  <section class="service" style="top:782px">
    <div class="service-head">
      <span class="service-icon"><svg width="24" height="22" viewBox="0 0 24 22"><path d="M6 2h16l-4 18H2z" fill="var(--ink)"/><path d="M12 2l-3 18M4 11h16" stroke="#fff" stroke-width="1.5"/></svg></span>
      <h3 class="service-name">Floor Cleaning</h3>
    </div>
    <p class="service-text">Marble Cleaning &amp; Polishing. Tile &amp; Grout Cleaning. Hardwood Floors Services. Vinyl Floors.</p>
  </section>

  <section class="service" style="top:896px">
    <div class="service-head">
      <span class="service-icon"><svg width="22" height="22" viewBox="0 0 22 22"><rect x="1.5" y="1.5" width="19" height="19" fill="none" stroke="var(--ink)" stroke-width="3"/><path d="M11 2v18M2 11h18" stroke="var(--ink)" stroke-width="2.5"/></svg></span>
      <h3 class="service-name">Window Cleaning</h3>
    </div>
    <p class="service-text">Regular, Reliable Window Cleaning. Hard To Reach Windows. Single 7 Multi-Storey. Frames and Glass Cleaned.</p>
  </section>

  <section class="service" style="top:1006px">
    <div class="service-head">
      <span class="service-icon"><svg width="26" height="18" viewBox="0 0 26 18"><path d="M2 16C2 8 8 2 14 4c3 1 2 6 6 6h4v6z" fill="var(--ink)"/></svg></span>
      <h3 class="service-name">Carpet Cleaning</h3>
    </div>
    <p class="service-text">The BRAM Dry Extraction Carpet Cleaning System uses environmentally preferred, Blue Crest Certified cleaning products that deep cleans your carpets and textured hard floors quickly and easily.</p>
  </section>

  <div class="side-photo dusting" role="img" aria-label="Gloved hand wiping a glossy surface with a yellow cloth"></div>
  <div class="side-photo window" role="img" aria-label="Hand cleaning a window pane with a blue cloth"></div>
  <div class="side-photo carpet" role="img" aria-label="Dry extraction carpet cleaning machine working on a carpet"></div>

  <footer class="footer">
    <div class="footer-phone-band"></div>
    <div class="cta">CALL US NOW FOR A FREE ESTIMATE!</div>
    <div class="phone">
      <svg width="30" height="30" viewBox="0 0 30 30"><circle cx="15" cy="15" r="13.5" fill="none" stroke="#fff" stroke-width="2"/><path d="M10 8.5c-1.5 1-2 2.5-1 5 1.5 3.5 4 6 7.5 7.5 2.5 1 4 .5 5-1l-2.5-2.5-2 1c-2-1-3.5-2.5-4.5-4.5l1-2z" fill="#fff"/></svg>
      <span>012 555 0148</span>
    </div>
  </footer>
</div>
</body>
</html>
```